Graniteway Surface Works, Inc. Business Card

New business, we do epoxy, polishing concrete, underlayment, fluid applied flooring, sound proofing, double sided, will need 3 sets of cards with 3 different names and phone numbers.
Company: Graniteway Surface Works, Inc.
Address and Phone: 6339 Charlotte Pike PMB 2183Nashville, TN 38514
(615) 418-3927
www.granitewaysurfaceworks.example

Target Market(s)

General Contractors, Contractors, Architects

Contact Information for Business Card

1st Card: Devon Halvorsen C. 708.214.5873 e. devon@granitewaysurfaceworks.example
Vice President
2nd Card: Morgan Prescoe C. 708.389.6145 e. morgan@granitewaysurfaceworks.example
President
3rd Card: Bo Vu C. 405.631.8207 e. bo@granitewaysurfaceworks.example
Managing Partner

Font styles to use
Serif
Sans Serif

Requirements
Must have
• Professional Clean Design, Implement colors from Logo or nicely contrasting
Nice to have
• N/A

```html
<!DOCTYPE html>
<html lang="en">
<head>
<meta charset="utf-8">
<title>Graniteway Surface Works – Business Card</title>
<link rel="stylesheet" href="https://fonts.googleapis.com/css2?family=Arimo:wght@400;700&family=Montserrat:wght@500&display=swap">
<style>
  :root {
    --stage: #cdcdcd;
    --card-white: #ffffff;
    --brand-green: #6aa04e;
    --brand-blue: #1c63b7;
    --ink: #1e1e1e;
    --rule-green: #8fbf6f;
  }
  * { margin: 0; padding: 0; box-sizing: border-box; }
  html, body { width: 1200px; height: 788px; overflow: hidden; }
  body {
    background: var(--stage);
    font-family: "Arimo", Arial, sans-serif;
    position: relative;
  }
  .card {
    position: absolute;
    top: 244px;
    width: 525px;
    height: 300px;
    border-radius: 22px;
    overflow: hidden;
    box-shadow: 0 14px 30px rgba(0,0,0,0.25);
  }
  .card--front { left: 45px; background: var(--card-white); }
  .card--back { left: 630px; background: var(--brand-green); }

  .front-wave { position: absolute; inset: 0; }

  .brand {
    position: absolute;
    display: flex;
    align-items: center;
    gap: 9px;
    font-family: "Montserrat", Arial, sans-serif;
    font-weight: 500;
    letter-spacing: 0.02em;
    line-height: 1.15;
  }
  .brand__mark { flex: none; }
  .card--front .brand {
    left: 34px; top: 92px;
    width: 180px;
    font-size: 15px;
    color: var(--ink);
  }
  .card--front .brand__mark { width: 16px; height: 16px; background: var(--brand-blue); }

  .divider {
    position: absolute;
    left: 222px; top: 52px;
    width: 1px; height: 112px;
    background: var(--rule-green);
  }

  .contact {
    position: absolute;
    left: 238px; top: 36px;
    color: var(--ink);
    font-size: 12.5px;
    line-height: 1.32;
  }
  .contact__name {
    font-size: 19px;
    font-weight: 700;
    line-height: 1.1;
  }
  .contact__first { color: var(--brand-blue); }
  .contact__last { color: var(--brand-green); }
  .contact__title { font-size: 13px; margin-bottom: 6px; }
  .contact__address { margin-bottom: 4px; }
  .contact__line { display: flex; align-items: center; gap: 6px; white-space: nowrap; }
  .contact__icon { width: 11px; height: 11px; flex: none; }

  .card--back .brand {
    left: 0; right: 0; top: 0; bottom: 0;
    justify-content: center;
    flex-direction: column;
    gap: 16px;
    color: var(--card-white);
    font-size: 30px;
    text-align: center;
  }
  .card--back .brand__mark {
    width: 52px; height: 52px;
    border: 6px solid var(--card-white);
  }
</style>
</head>
<body>

  <section class="card card--front">
    <svg class="front-wave" width="525" height="300" viewBox="0 0 525 300">
      <path d="M0 300 C 210 300, 330 250, 525 212 L525 300 Z" fill="var(--brand-green)"/>
      <path d="M0 300 C 210 300, 330 250, 525 212" fill="none" stroke="var(--card-white)" stroke-width="4"/>
      <path d="M20 297 C 215 295, 330 244, 525 205" fill="none" stroke="var(--brand-blue)" stroke-width="5"/>
    </svg>

    <div class="brand">
      <span class="brand__mark"></span>
      <span class="brand__name">Graniteway Surface Works</span>
    </div>

    <div class="divider"></div>

    <div class="contact">
      <p class="contact__name"><span class="contact__first">Morgan</span> <span class="contact__last">Prescoe</span></p>
      <p class="contact__title">President</p>
      <p class="contact__address">4812 Wendover Ridge PMB<br>7416Nashville, TN 38514</p>
      <p class="contact__line">
        <svg class="contact__icon" viewBox="0 0 12 12"><circle cx="6" cy="6" r="6" fill="var(--brand-blue)"/><path d="M4 3.2 L5.2 4.6 L4.6 5.4 Q5.4 7 6.8 7.6 L7.6 7 L9 8.2 L8.2 9.2 Q5.6 9 3.2 5.6 Q3 4.2 4 3.2Z" fill="#fff"/></svg>
        708.389.6145
      </p>
      <p class="contact__line">
        <svg class="contact__icon" viewBox="0 0 12 12"><circle cx="6" cy="6" r="6" fill="var(--brand-blue)"/><rect x="2.8" y="3.8" width="6.4" height="4.4" fill="#fff"/><path d="M2.8 3.8 L6 6.4 L9.2 3.8" fill="none" stroke="var(--brand-blue)" stroke-width="0.8"/></svg>
        morgan@granitewaysurfaceworks.example
      </p>
      <p class="contact__line">
        <svg class="contact__icon" viewBox="0 0 12 12"><circle cx="6" cy="6" r="6" fill="var(--brand-blue)"/><circle cx="6" cy="6" r="3.4" fill="none" stroke="#fff" stroke-width="0.9"/><path d="M2.6 6 H9.4 M6 2.6 Q4.2 6 6 9.4 M6 2.6 Q7.8 6 6 9.4" fill="none" stroke="#fff" stroke-width="0.8"/></svg>
        www.granitewaysurfaceworks.example
      </p>
    </div>
  </section>

  <section class="card card--back">
    <div class="brand">
      <span class="brand__mark"></span>
      <span class="brand__name">Graniteway<br>Surface Works</span>
    </div>
  </section>

</body>
</html>
```